Veltrane Application Brochures

Hi,

We are a semiconductor company looking to create application brochures to show a comprehensive overview of our product portfolio. The applications are as follows:
• Audio
• Automotive
• Proximity
• Smart Buildings
• Smartphones
• TV and Set-Top
• Wearables

To keep things consistent, we would like one template which we can use for the 7 application brochures listed above.

Our company website is:
https://www.veltrane-semiconductor.example/company/about-us

Veltrane Semiconductor provides highly integrated standard and custom mixed-signal ICs, optimized for smartphone, computing, IoT, SSL, and smart home applications.

Attaching what we had in the past for the "charging" application so you can see the type of information we will have.

Thank you

Marta

```html
<!DOCTYPE html>
<html lang="en">
<head>
<meta charset="utf-8">
<title>Veltrane Application Brochures</title>
<link href="https://fonts.googleapis.com/css2?family=Lato:wght@300;400;700&family=Zilla+Slab:wght@300;400&display=swap" rel="stylesheet">
<style>
  :root{
    --brand:#1aa7cf;
    --brand-light:#7fcfe6;
    --ink:#3a3a3a;
    --icon-grey:#8e8e8e;
    --icon-shadow:#5e5e5e;
    --brand-shadow:#0f7fa0;
    --paper:#ffffff;
    --backdrop:#e6e6e6;
  }
  *{box-sizing:border-box;margin:0;padding:0}
  html,body{width:1200px;height:1200px;overflow:hidden;background:var(--backdrop)}
  body{position:relative;font-family:'Lato',sans-serif;color:var(--ink)}
  .page{position:absolute;top:182px;width:532px;height:746px;background:var(--paper);overflow:hidden}
  .page--audio{left:40px}
  .page--auto{left:630px}
  .abs{position:absolute}
  .brand{position:absolute;display:flex;align-items:center;gap:8px}
  .brand__dot{width:30px;height:30px;border-radius:50%;background:var(--brand)}
  .brand__name{font-family:'Lato',sans-serif;font-weight:400;font-size:34px;color:var(--brand);letter-spacing:-0.5px;line-height:1}
  .photo{position:absolute}
  .band{position:absolute;left:0;width:532px;background:var(--brand)}
  .footer-bar{position:absolute;left:0;bottom:0;width:532px;height:14px;background:var(--brand)}
  .body-text{font-size:7.4px;line-height:1.42;text-align:justify;color:var(--ink)}
  .on-brand{color:#fff}
  .slab{font-family:'Zilla Slab',serif;font-weight:300;color:var(--brand)}
  .rule{position:absolute;height:2px;background:var(--brand)}
  /* audio */
  .hero-title{font-family:'Zilla Slab',serif;font-weight:300;font-size:38px;color:#fff;line-height:1}
  .hero-sub{font-family:'Lato',sans-serif;font-weight:300;font-size:23px;color:#fff;line-height:1}
  .feature{position:absolute;top:366px;width:108px}
  .feature__icon{position:relative;width:82px;height:80px;margin:0 0 0 5px}
  .feature__icon::after{content:"";position:absolute;left:5px;top:5px;width:82px;height:80px;background:var(--shade);z-index:0}
  .feature__icon svg{position:relative;z-index:1;display:block;width:82px;height:80px;background:var(--fill)}
  .feature__icon--blue{--fill:var(--brand);--shade:var(--brand-shadow)}
  .feature__icon--grey{--fill:var(--icon-grey);--shade:var(--icon-shadow)}
  .feature__label{margin-top:14px;text-align:center;font-family:'Zilla Slab',serif;font-weight:300;font-size:11px;color:var(--brand)}
  .feature__text{margin-top:6px;font-size:7px;line-height:1.36;text-align:justify}
  .bullets{list-style:none;font-size:7px;line-height:1.3}
  .bullets li{position:relative;padding-left:10px;margin-bottom:7px}
  .bullets li::before{content:"";position:absolute;left:1px;top:2.5px;width:3.5px;height:3.5px;border-radius:50%;background:var(--brand)}
  /* automotive */
  .section-title{font-family:'Zilla Slab',serif;font-weight:300;font-size:26px;color:var(--brand);text-align:center;width:532px;left:0}
  .sub-title{font-family:'Zilla Slab',serif;font-weight:300;font-size:12px;color:var(--brand);line-height:1.3}
  .band-title{font-family:'Zilla Slab',serif;font-weight:400;font-size:10.5px;color:#fff}
</style>
</head>
<body>

<section class="page page--audio">
  <div class="brand" style="left:32px;top:48px"><span class="brand__dot"></span><span class="brand__name">Veltrane</span></div>

  <div class="band" style="top:111px;height:222px"></div>
  <div class="photo" role="img" aria-label="Photo of a man in sunglasses and headphones listening to music on his phone" style="left:255px;top:18px;width:277px;height:315px;background:linear-gradient(160deg,#d9d4c9 0%,#a77a5c 40%,#5b3b2a 70%,#c9c3b8 100%);clip-path:polygon(30% 0,80% 0,100% 20%,100% 100%,0 100%,12% 55%)"></div>

  <div class="abs" style="left:34px;top:130px"><h1 class="hero-title">Audio</h1></div>
  <div class="abs" style="left:32px;top:176px"><p class="hero-sub">Crystal clear audio</p></div>
  <div class="rule" style="left:32px;top:206px;width:78px;background:#fff"></div>
  <p class="abs body-text on-brand" style="left:32px;top:211px;width:222px">We offer a range of low power, hi-fi audio CODECs and class Ds with different features and packages suitable for a variety of low power, digital portable audio products. Our CODECs are designed to offer different levels of dynamic range and improve the power consumption for the record and playback paths by optimizing the always ON mode and utilizing efficient charge pump technologies.</p>

  <div class="feature" style="left:20px">
    <div class="feature__icon feature__icon--blue">
      <svg viewBox="0 0 82 80"><rect x="26" y="16" width="22" height="44" rx="3" fill="none" stroke="#fff" stroke-width="3"/><circle cx="37" cy="54" r="2" fill="#fff"/><path d="M44 28 L58 24 V46" fill="none" stroke="#fff" stroke-width="3"/><circle cx="54" cy="47" r="4.5" fill="#fff"/><circle cx="42" cy="50" r="4.5" fill="#fff"/></svg>
    </div>
    <p class="feature__label">Audio Codecs</p>
    <p class="feature__text">Low power, Hi-Fi audio CODECs with different features and in packages suitable for a variety of digital and low power audio products.</p>
  </div>
  <div class="feature" style="left:152px">
    <div class="feature__icon feature__icon--grey">
      <svg viewBox="0 0 82 80"><path d="M18 52 V42 a23 23 0 0 1 46 0 V52" fill="none" stroke="#fff" stroke-width="3.5"/><rect x="14" y="46" width="9" height="16" rx="3" fill="#fff"/><rect x="59" y="46" width="9" height="16" rx="3" fill="#fff"/><path d="M30 40 a15 15 0 0 1 22 0 M34 45 a9 9 0 0 1 14 0" fill="none" stroke="#fff" stroke-width="3"/><circle cx="41" cy="51" r="2.5" fill="#fff"/></svg>
    </div>
    <p class="feature__label">Wireless Audio</p>
    <p class="feature__text">Our short range wireless ICs deliver enhanced efficiency to devices ranging from DECT phones and wireless headsets to game controllers providing improved battery life</p>
  </div>
  <div class="feature" style="left:284px">
    <div class="feature__icon feature__icon--blue">
      <svg viewBox="0 0 82 80"><path d="M22 42 a19 19 0 0 1 38 0" fill="none" stroke="#fff" stroke-width="4"/><rect x="16" y="38" width="10" height="16" rx="4" fill="#fff"/><rect x="56" y="38" width="10" height="16" rx="4" fill="#fff"/><path d="M61 54 Q60 64 46 64" fill="none" stroke="#fff" stroke-width="3"/><rect x="40" y="61" width="7" height="5" rx="2" fill="#fff"/></svg>
    </div>
    <p class="feature__label">USB Audio</p>
    <p class="feature__text">Our platform solutions range from low to high-end Talkwire compliant USB headsets and headphones allowing development, software, and hardware resources to be shared across the product range.</p>
  </div>
  <div class="feature" style="left:412px">
    <div class="feature__icon feature__icon--grey">
      <svg viewBox="0 0 82 80" fill="#fff"><rect x="22" y="18" width="2.5" height="44"/><rect x="35" y="18" width="2.5" height="44"/><rect x="48" y="18" width="2.5" height="44"/><rect x="61" y="18" width="2.5" height="44"/><rect x="18" y="28" width="10" height="6"/><rect x="31" y="44" width="10" height="6"/><rect x="44" y="24" width="10" height="6"/><rect x="57" y="38" width="10" height="6"/></svg>
    </div>
    <p class="feature__label">Audio Amplifiers</p>
    <p class="feature__text">Powerful, highly efficient, low EMI mono filterless class D speaker driver ICs for 1S and 2S portable applications.</p>
  </div>

  <div class="photo" role="img" aria-label="Photo of a smiling woman wearing headphones in an autumn park" style="left:22px;top:570px;width:187px;height:138px;background:linear-gradient(120deg,#c98a3e,#e8c48a 45%,#a4452f 80%,#7a2a20)"></div>
  <h2 class="abs slab" style="left:219px;top:572px;font-size:12px">At the forefront of innovation</h2>
  <p class="abs body-text" style="left:219px;top:591px;width:292px">With a long legacy of delivering different power management designs for industry-leading mobile phone manufacturers and portable consumer OEMs, we optimize all aspects of design including electrical, thermal and packaging considerations. These designs offer unprecedented integration with multiple power management and analog functions on the chip, including:</p>
  <ul class="abs bullets" style="left:219px;top:646px;width:160px">
    <li>Programmable high-performance LDOs</li>
    <li>High-efficiency DC-DC voltage converters</li>
    <li>Intelligent battery charging circuits</li>
  </ul>
  <ul class="abs bullets" style="left:386px;top:643px;width:126px">
    <li>Sensor ADCs</li>
    <li>USB interfaces</li>
    <li>Integrated high performance, low power audio</li>
  </ul>
  <div class="footer-bar"></div>
</section>

<section class="page page--auto">
  <div class="brand" style="left:26px;top:22px"><span class="brand__dot"></span><span class="brand__name">Veltrane</span></div>
  <div class="photo" role="img" aria-label="Photo of a car dashboard infotainment unit showing navigation" style="left:0;top:75px;width:532px;height:216px;background:linear-gradient(180deg,#3a3b3d,#1d1e20 55%,#5a5c5e)"></div>

  <h1 class="abs section-title" style="top:300px">Automotive</h1>
  <h2 class="abs sub-title" style="left:21px;top:340px">Flexibility and scalability now come as standard</h2>
  <div class="rule" style="left:21px;top:358px;width:72px"></div>
  <p class="abs body-text" style="left:21px;top:367px;width:492px;font-size:7px">The continued convergence of mobile technologies with vehicles means car infotainment systems are rapidly evolving into platforms that combine entertainment, 3D navigation, and driver safety information incorporating all round view camera processing. To meet the demanding connected car power management needs of today's vehicle manufacturers and system suppliers, we offer a range of automotive qualified system-PMICs and sub-PMICs designed to meet the stringent quality and reliability requirements of the automotive industry.</p>

  <div class="band" style="top:422px;height:120px"></div>
  <div class="photo" role="img" aria-label="Photo of a driver touching a large central display in a modern car" style="left:0;top:422px;width:175px;height:120px;background:linear-gradient(110deg,#d8d8d8,#6b6f74 40%,#1e2a36 70%,#3b7fa6)"></div>
  <h3 class="abs band-title" style="left:185px;top:432px">Accelerate your next generation automotive platform development</h3>
  <p class="abs body-text on-brand" style="left:185px;top:447px;width:332px;font-size:7px">Discover the benefits of Veltrane's highly integrated automotive PMICs with powerful built-in configurability engines. Veltrane's unique partitioning into system and sub-PMICs offers the advantages of scalability and flexibility whilst distributing the power dissipation in adverse temperature environments. This offers the system designer confidence to customize a reference design when new peripherals are added by resolving power sequencing, thermal and system control challenges. The end result is a secure, reliable, highly optimized but yet differentiated power supply design.</p>
  <p class="abs body-text on-brand" style="left:185px;top:518px;width:332px;font-size:7px;text-align:left">All Veltrane automotive power management products are qualified to AEC-Q100 as designated by the "-A" suffix</p>

  <h2 class="abs sub-title" style="left:21px;top:559px;width:220px">Leading technology for automotive platforms</h2>
  <div class="rule" style="left:21px;top:594px;width:64px"></div>
  <p class="abs body-text" style="left:21px;top:599px;width:222px;font-size:7px">Our leading-edge core regulator technology, developed for Corvane and Mirelto-based processors, combined with our experience as a supplier of automotive parts gives it unparalleled experience of delivering to automotive customers. Our technology and quality assurance processes enable us to deliver the highest level of performance, quality and reliability for customers' AEC-Q100 applications</p>
  <p class="abs body-text" style="left:21px;top:669px;width:222px;font-size:7px">Our unique system and sub-PMIC segmentation offers the ability to scale the power supply to match the expected processor demand. The built-in configurability helps maximize software reuse, reducing verification cycles, and offers customers the ability to optimize system BOM whilst addressing multiple tiers of end product.</p>

  <div class="photo" role="img" aria-label="Block diagram of an automotive infotainment system linking displays, modules and network interfaces" style="left:268px;top:564px;width:246px;height:156px;background:linear-gradient(160deg,#eef6f9,#d3ebf3 50%,#e4e8ea)"></div>
  <div class="footer-bar"></div>
</section>

</body>
</html>
```